the letter head should have the logo ( may be top left), " Fenwick Ridge Institute" (may be top/middle ) and the two clinics info in a vertical column ( along the left side of the page )

Target Market(s)

other physicians and official letters

Requirements
Must have
• the info provided in the attachements

```html
<!DOCTYPE html>
<html lang="en">
<head>
<meta charset="utf-8">
<title>Fenwick Ridge Institute Letterhead</title>
<link rel="stylesheet" href="https://fonts.googleapis.com/css2?family=Lato:wght@400;700&display=swap">
<style>
  :root {
    --backdrop: #ececec;
    --paper: #ffffff;
    --magenta: #a3195b;
    --slate: #3a4752;
    --ink: #3b3b3b;
  }
  * { margin: 0; padding: 0; box-sizing: border-box; }
  html, body {
    width: 1200px;
    height: 1200px;
    overflow: hidden;
    background: var(--backdrop);
    font-family: "Lato", sans-serif;
  }
  .letterhead {
    position: absolute;
    left: 136px;
    top: 0;
    width: 927px;
    height: 1200px;
    background: var(--paper);
  }
  .brand {
    position: absolute;
    left: 88px;
    top: 50px;
    display: flex;
    align-items: center;
    gap: 12px;
  }
  .brand-square {
    width: 58px;
    height: 58px;
    background: var(--slate);
    flex: none;
  }
  .brand-name {
    font-weight: 400;
    font-size: 24px;
    line-height: 1.15;
    color: var(--slate);
  }
  .office-column {
    position: absolute;
    left: 88px;
    top: 150px;
    width: 170px;
    padding-right: 14px;
    border-right: 1px solid var(--magenta);
    display: flex;
    flex-direction: column;
    gap: 16px;
  }
  .office {
    color: var(--ink);
    font-size: 13px;
    line-height: 15px;
  }
  .office + .office {
    padding-top: 16px;
    border-top: 1px solid var(--magenta);
  }
  .office-title {
    font-weight: 700;
    font-size: 15px;
    color: var(--magenta);
    margin-bottom: 6px;
  }
  .contact-line {
    display: flex;
    align-items: flex-start;
    gap: 7px;
  }
  .contact-line--address { margin-top: 4px; }
  .contact-icon {
    width: 9px;
    height: 9px;
    margin-top: 3px;
    flex: none;
    fill: var(--magenta);
  }
</style>
</head>
<body>
<main class="letterhead">
  <header class="brand">
    <span class="brand-square"></span>
    <span class="brand-name">Fenwick Ridge<br>Institute</span>
  </header>

  <aside class="office-column">
    <section class="office">
      <h2 class="office-title">Little Rock Office</h2>
      <p class="contact-line">
        <svg class="contact-icon" viewBox="0 0 10 10" aria-hidden="true"><path d="M2 0.5 L3.6 2.6 L2.8 3.6 C3.5 5 4.9 6.4 6.4 7.2 L7.4 6.4 L9.5 8 L8.4 9.5 C4.5 9.3 0.7 5.5 0.5 1.6 Z"/></svg>
        <span>501-555-0174</span>
      </p>
      <p class="contact-line">
        <svg class="contact-icon" viewBox="0 0 10 10" aria-hidden="true"><path d="M2.5 0.5 H7.5 V3 H9.5 V9.5 H0.5 V3 H2.5 Z M3.5 1.5 V3 H6.5 V1.5 Z M2 5 V6 H3 V5 Z M4 5 V6 H5 V5 Z M6 5 V6 H8 V5 Z"/></svg>
        <span>501-555-0136</span>
      </p>
      <p class="contact-line contact-line--address">
        <svg class="contact-icon" viewBox="0 0 10 10" aria-hidden="true"><path d="M5 0 C2.8 0 1.5 1.6 1.5 3.5 C1.5 6 5 10 5 10 C5 10 8.5 6 8.5 3.5 C8.5 1.6 7.2 0 5 0 Z M5 2.2 A1.3 1.3 0 1 1 5 4.8 A1.3 1.3 0 1 1 5 2.2 Z"/></svg>
        <span>218 W. Ashford Ave.<br>Suite 310, 72201</span>
      </p>
    </section>

    <section class="office">
      <h2 class="office-title">Pine Bluff Office</h2>
      <p class="contact-line">
        <svg class="contact-icon" viewBox="0 0 10 10" aria-hidden="true"><path d="M2 0.5 L3.6 2.6 L2.8 3.6 C3.5 5 4.9 6.4 6.4 7.2 L7.4 6.4 L9.5 8 L8.4 9.5 C4.5 9.3 0.7 5.5 0.5 1.6 Z"/></svg>
        <span>870-555-0188</span>
      </p>
      <p class="contact-line">
        <svg class="contact-icon" viewBox="0 0 10 10" aria-hidden="true"><path d="M2.5 0.5 H7.5 V3 H9.5 V9.5 H0.5 V3 H2.5 Z M3.5 1.5 V3 H6.5 V1.5 Z M2 5 V6 H3 V5 Z M4 5 V6 H5 V5 Z M6 5 V6 H8 V5 Z"/></svg>
        <span>870-555-0122</span>
      </p>
      <p class="contact-line contact-line--address">
        <svg class="contact-icon" viewBox="0 0 10 10" aria-hidden="true"><path d="M5 0 C2.8 0 1.5 1.6 1.5 3.5 C1.5 6 5 10 5 10 C5 10 8.5 6 8.5 3.5 C8.5 1.6 7.2 0 5 0 Z M5 2.2 A1.3 1.3 0 1 1 5 4.8 A1.3 1.3 0 1 1 5 2.2 Z"/></svg>
        <span>1625 N. Hazel St.<br>Pine Bluff 71601</span>
      </p>
    </section>
  </aside>
</main>
</body>
</html>
```